ROLL-ON-VERANDA Business Card Design

Please do not submit more than one design per designer. Both the front and the back must be submitted as a single design. Please use all of the attached files to design a two-sided business card. Do not use tiny text that is hard to read. Do not put text or images too close to the edges where it might get cut off during printing. The card should be horizontal. Please do not send me the same design that I attached showing the business information. Be creative.

One file is marked as the primary logo for company. Other files are marked as secondary. All logos should be incorporated into the design with a focus on the primary one being bigger.

```html
<!DOCTYPE html>
<html lang="en">
<head>
<meta charset="utf-8">
<title>ROLL-ON-VERANDA Business Card</title>
<link rel="stylesheet" href="https://fonts.googleapis.com/css2?family=Lexend:wght@400;600;700&family=Exo+2:ital,wght@1,800&display=swap">
<style>
  :root {
    --backdrop: #d6d6d6;
    --card: #ffffff;
    --ink: #111111;
    --paper-text: #ffffff;
  }
  html, body {
    margin: 0;
    width: 1200px;
    height: 1200px;
    overflow: hidden;
    background: var(--backdrop);
  }
  .card {
    position: absolute;
    left: 150px;
    width: 900px;
    height: 527px;
    background: var(--card);
    box-shadow: 0 3px 8px rgba(0,0,0,0.25);
    overflow: hidden;
    font-family: "Lexend", sans-serif;
    color: var(--ink);
  }
  .card--front { top: 56px; }
  .card--back { top: 616px; }
  .card__shapes {
    position: absolute;
    inset: 0;
  }
  .tagline {
    position: absolute;
    left: 57px;
    top: 55px;
    margin: 0;
    font-weight: 600;
    font-size: 22.5px;
    line-height: 29px;
    letter-spacing: 0.2px;
    text-transform: uppercase;
  }
  .captain {
    position: absolute;
    left: 57px;
    top: 168px;
    color: var(--paper-text);
  }
  .captain__name {
    margin: 0 0 16px;
    font-family: "Exo 2", sans-serif;
    font-style: italic;
    font-weight: 800;
    font-size: 26px;
    letter-spacing: 1.2px;
    text-decoration: underline;
    text-decoration-thickness: 2px;
    text-underline-offset: 4px;
  }
  .captain__credentials {
    margin: 0;
    padding: 0;
    list-style: none;
    font-size: 19px;
    line-height: 25px;
    font-weight: 400;
  }
  .captain__credentials li::before { content: "• "; }
  .contact {
    position: absolute;
    left: 497px;
    top: 355px;
    margin: 0;
    padding: 0;
    list-style: none;
    font-size: 21px;
    line-height: 35px;
  }
  .contact li { display: flex; align-items: center; gap: 12px; }
  .contact svg { width: 16px; height: 16px; fill: var(--ink); }
  .brand {
    position: absolute;
    left: 0;
    right: 0;
    top: 230px;
    margin: 0;
    text-align: center;
    font-weight: 700;
    font-size: 56px;
    letter-spacing: 1px;
    color: var(--ink);
  }
</style>
</head>
<body>
  <section class="card card--front">
    <svg class="card__shapes" viewBox="0 0 900 527" aria-hidden="true">
      <polygon class="name-band" points="0,146 627,146 422,359 0,359" fill="var(--ink)"/>
      <polyline class="contact-frame" points="905,309 512,309 350,482 905,482" fill="none" stroke="var(--ink)" stroke-width="3"/>
    </svg>
    <p class="tagline">Providing hands-on boat training, captaining services<br>and deliveries in the Pinellas Country area</p>
    <div class="captain">
      <h1 class="captain__name">CAPTAIN DANA R.HOLLOWAY</h1>
      <ul class="captain__credentials">
        <li>USCG Licensed master Captain</li>
        <li>NSBC Certified Instructor</li>
        <li>Graduate Degree</li>
        <li>Veteran</li>
      </ul>
    </div>
    <ul class="contact">
      <li><svg viewBox="0 0 16 16"><path d="M3.5 1.5l2.5 3-1.5 1.8c.8 1.8 2.2 3.2 4 4l1.8-1.5 3 2.5-1.5 2.5C7 13.5 2.5 9 1 3z"/></svg>(555) 014-2290</li>
      <li><svg viewBox="0 0 16 16"><path d="M1 3.5h14v9H1z M1.5 4l6.5 5 6.5-5" stroke="#fff" stroke-width="1.2"/></svg>service.Roll-On-Veranda.com</li>
      <li><svg viewBox="0 0 16 16"><circle cx="8" cy="8" r="7"/><path d="M1 8h14M8 1c-3 3-3 11 0 14M8 1c3 3 3 11 0 14" stroke="#fff" stroke-width="1" fill="none"/></svg>www.Roll-On-Veranda.com</li>
    </ul>
  </section>

  <section class="card card--back">
    <p class="brand">ROLL-ON-VERANDA</p>
  </section>
</body>
</html>
```